Northwind Crate Traders Needs a FRESH website

We would like a creative minded designer to take on the task to Re-design our website. Its a simple 5-7 pages. With no cart, no complex html. Just plain information about our company and products we import and export. Pictures added to the product section. Since Our logo its Blue, we would like the designer to use complementing colors in order to make the website look cleaner and modern.

Target Market(s)

The target audience will be companies looking to purchase plastic related products. Companies looking to purchase large quantities of plastic containers (Shampoo bottles, caps, sprayers, mist sprayers, cosmetic containers etc).

Industry/Entity Type

It Company

Font styles to use
Sans Serif

Requirements
Must have
• We have a section in which we would like to add pictures of some of the products we carry, therefore having an easy and clean way to navigate through the pictures will be a plus.

```html
<!DOCTYPE html>
<html lang="en">
<head>
<meta charset="utf-8">
<title>Northwind Crate Traders</title>
<link href="https://fonts.googleapis.com/css2?family=Arimo:wght@400&family=Heebo:wght@300;400&family=Roboto+Condensed:wght@400&display=swap" rel="stylesheet">
<style>
:root{
  --brand-blue:#1f86d2;
  --brand-blue-dark:#1a69a8;
  --link-blue:#2a6fb5;
  --ink:#1e1e1e;
  --text:#333333;
  --page:#ececec;
  --panel:#ffffff;
  --accent-red:#e01b22;
  --rule:#b5b5b5;
}
*{margin:0;padding:0;box-sizing:border-box}
html,body{width:1082px;height:1200px;overflow:hidden}
body{position:relative;background:var(--page);font-family:"Heebo",Helvetica,Arial,sans-serif;color:var(--text)}
.abs{position:absolute}
.top-bar{left:0;top:0;width:1082px;height:8px;background:var(--brand-blue)}
.header{left:24px;top:12px;width:1034px;height:137px;background:linear-gradient(#ffffff,#f3f3f3);border-radius:8px 8px 0 0}
.brand{left:34px;top:20px;width:210px;text-align:center}
.brand-mark{width:76px;height:76px;border-radius:50%;background:var(--brand-blue);margin:0 auto 2px}
.brand-name{font-family:"Heebo",sans-serif;font-weight:400;color:#3a3a3a;font-size:26px;line-height:28px;letter-spacing:-.3px}
.brand-name small{display:block;font-size:15px;letter-spacing:4px;line-height:16px}
.nav{right:26px;top:119px;display:flex;font-family:"Arimo",Arial,sans-serif;font-size:12.5px;color:#111}
.nav a{color:inherit;text-decoration:none;padding:0 13px;border-left:1px solid #222;line-height:17px}
.nav a:first-child{border-left:0}
.nav a:last-child{padding-right:0}
.dotted{left:0;width:1082px;height:3px;border-top:2px dotted #9a9a9a}
.hero{left:0;top:151px;width:1082px;height:395px;background:linear-gradient(100deg,#e4e8ee 0%,#c9d3e0 30%,#aebfd6 60%,#c8d5e6 80%,#9fb6d6 100%)}
.hero-title{left:50px;top:408px;font-size:46px;font-weight:300;color:var(--ink);line-height:52px;letter-spacing:-.5px}
.hero-title span{display:inline-block;background:var(--ink);color:#fff;padding:0 5px;margin-left:-5px;margin-top:2px}
.slider-dots{left:957px;top:511px;display:flex;gap:12px}
.dot{width:22px;height:22px;border-radius:50%;background:#fff;display:flex;align-items:center;justify-content:center}
.dot i{width:12px;height:12px;border-radius:50%;background:var(--brand-blue)}
.dot.active i{background:#111}
.content-bg{left:24px;top:552px;width:1034px;height:548px;background:linear-gradient(#eaeaea,#f1f1f1 60%,#e6e6e6)}
.welcome{left:42px;top:570px;width:661px}
.welcome h1{font-size:31px;font-weight:300;color:var(--ink);line-height:36px}
.welcome h2{font-size:17px;font-weight:300;color:var(--link-blue);line-height:20px;padding-left:2px;padding-bottom:2px;border-bottom:1px solid #333}
.welcome p{font-size:14.6px;font-weight:300;line-height:22px;margin-top:8px;color:#222}
.more{left:599px;top:795px;width:104px;height:30px;background:#1d1d1d;display:flex}
.more span{flex:1;color:var(--brand-blue);font-size:20px;font-weight:300;line-height:30px;text-align:center}
.more b{width:26px;background:var(--brand-blue);display:flex;align-items:center;justify-content:center}
.mission{left:718px;top:558px;width:336px;height:270px;background:var(--panel)}
.mission h3{font-size:30px;font-weight:300;color:var(--ink);margin:14px 10px 0 22px;line-height:36px}
.mission hr{border:0;border-top:1px solid var(--brand-blue);margin:18px 9px 0 10px}
.mission p{font-size:14.6px;font-weight:300;line-height:20px;margin:8px 14px 0 18px;color:#222}
.mission-img{left:730px;top:721px;width:311px;height:91px;background:linear-gradient(90deg,#3d6fb5,#9fc3ea 55%,#2a65b0);border:1px solid #2a5aa0}
.card{top:880px;width:322px;height:188px;background:#d3d3d3}
.card-img{position:absolute;left:8px;top:9px;width:306px;height:170px;border:1px solid #2a5aa0}
.card-label{position:absolute;left:4px;top:115px;width:298px;height:36px;background:rgba(255,255,255,.75);border-left:3px solid var(--accent-red);font-family:"Roboto Condensed",sans-serif;font-size:22px;line-height:36px;color:#111;padding-left:18px}
.footer{left:0;top:1100px;width:1082px;height:100px;background:var(--brand-blue);color:#fff}
.footer-text{left:65px;top:38px;font-size:12.5px;font-weight:300;line-height:17px}
.social{right:69px;top:34px;display:flex;gap:9px}
.social span{width:34px;height:34px;border-radius:50%;background:var(--brand-blue-dark);color:#fff;font-size:8.5px;display:flex;align-items:center;justify-content:center}
</style>
</head>
<body>
<div class="abs top-bar"></div>
<header class="abs header"></header>
<div class="abs brand">
  <div class="brand-mark"></div>
  <div class="brand-name">Northwind Crate<small>TRADERS</small></div>
</div>
<nav class="abs nav">
  <a href="#">HOME</a><a href="#">ABOUT US</a><a href="#">OUR PRODUCTS</a><a href="#">MISSION STATEMENT</a><a href="#">CONTACT US</a>
</nav>
<div class="abs dotted" style="top:147px"></div>
<div class="abs hero" role="img" aria-label="Plastic flakes, resin pellets, bottle preforms and clear PET bottles"></div>
<div class="abs hero-title">Looking to buy or sell plastic<br><span>material?</span></div>
<div class="abs slider-dots"><div class="dot active"><i></i></div><div class="dot"><i></i></div><div class="dot"><i></i></div></div>
<div class="abs dotted" style="top:546px"></div>

<div class="abs content-bg" role="img" aria-label="Faint row of plastic bottles in the background"></div>
<section class="abs welcome">
  <h1>Welcome To !</h1>
  <h2>Northwind Crate Traders</h2>
  <p>We should use the same text that is on the current website unless something else should be added. (Add an image of some sort depicting about us.&nbsp; Image of some products could do)</p>
  <p style="margin-top:22px">The current site seems too plain at the moment and I believe it is because of lack of text or images. We could add more links to the side of the page linking to images on the site or text explaining what some of the products we carry are.</p>
</section>
<a class="abs more" href="#"><span>MORE</span><b><svg width="8" height="10" viewBox="0 0 8 10"><path d="M2 1l4 4-4 4" fill="none" stroke="#fff" stroke-width="1.2"/></svg></b></a>

<aside class="abs mission">
  <h3>Mission Statement</h3>
  <hr>
  <p>We can use the same text that is on the cur-rent website unless something else should be added.</p>
</aside>
<div class="abs mission-img" role="img" aria-label="Books labelled vision, mission and values beside a pen"></div>

<div class="abs card" style="left:33px"><div class="card-img" role="img" aria-label="PET resin pellets spilling from a jar" style="background:linear-gradient(135deg,#e8dde6,#c9b8c4 50%,#f2eef2)"></div><div class="card-label" style="left:12px;top:124px">PET Resin</div></div>
<div class="abs card" style="left:380px"><div class="card-img" role="img" aria-label="Assorted clear, blue and green PET bottles" style="background:linear-gradient(#a9c3df,#8fb0d6 60%,#c7d6e6)"></div><div class="card-label" style="left:12px;top:124px">PET Containers / Bottles</div></div>
<div class="abs card" style="left:727px"><div class="card-img" role="img" aria-label="Steel bottle molds on blue stands" style="background:linear-gradient(#e4e4e4,#8a8a8a 50%,#d8dbe2)"></div><div class="card-label" style="left:12px;top:124px">Molds</div></div>

<footer class="abs footer">
  <div class="abs footer-text">NORTHWIND CRATE TRADERS<br>© 2014&nbsp; Privacy Policy</div>
  <div class="abs social"><span>Chatly</span><span>Feed</span><span>Chirpr</span><span>Circlo</span></div>
</footer>
</body>
</html>
```